Financial Sevices firm looking for Brochure design

Our company Veltmoor Capital and Holdings Limited (VeltHoldings)
i
Is an investment/advisory firm - www.veltholdings-grp.net
We invest in the energy sector in Africa and offer advisory services to Energy companies looking to invest in Africa. From oil and gas, to renewables (wind/solar). We are more focused on the "West African" Sub region
We need corporate brochure (Booklet style) to circulate to our corporate clients
We would like to see a design that considers the colours in our Logo (see website)
HI Guys, sorry been travelling. Seen some very good submissions and will be sending updates shortly
Reason: Dear Designers,
Thank you for participating in this project and for some of the great designs i've received so far. Unfortunately, due to the holidays, it has been difficult to consult with other members of my team. As a result, the project deadline is extended by about 12 days
I appreciate your understanding in the situation and looking forward to continuing the excellent collaboration in the coming days
Reason: Hi All,
Apologies for the multiple deadline extensions and thanks so much for all the designs which my team and I will be reviewing today and tomorrow.
We will be closing this project tomorrow by 6pm GMT (17th Jan 2014)
Thanks to all those that submitted such wonderful designs and goodluck!!
Project to be closed finally on 17th Jan 2014 at 6pm GMT
Banks, Investment Firms, Energy companies, Private Equity Funds
I have attached a Brochure that I created myself as an example of the type of information required but please also feel free to visit our website www.veltholdings-grp.net
Looking for any creative ideas you have to suplement the information provided.
Financial

```html
<!DOCTYPE html>
<html lang="en">
<head>
<meta charset="utf-8">
<title>VeltHoldings Brochure</title>
<link href="https://fonts.googleapis.com/css2?family=Arimo:wght@400;700&family=Oswald:wght@500;700&display=swap" rel="stylesheet">
<style>
:root{
  --bg:#060807;
  --red:#ff0000;
  --red-deep:#e0001b;
  --ink:#222222;
  --ink-soft:#444444;
  --grey-band:#4d5656;
  --grey-head:#3f4647;
  --panel-grey:#f3f4f4;
  --page-tail:#f3f6f6;
  --white:#ffffff;
  --black:#000000;
  --charcoal:#1b1b1b;
}
*{box-sizing:border-box;margin:0;padding:0}
html,body{width:1200px;height:1000px;overflow:hidden;background:var(--bg);font-family:"Arimo",Arial,sans-serif}
.canvas{position:relative;width:1200px;height:1000px}
.page{position:absolute;top:241px;width:351px;height:497px;background:var(--white);overflow:hidden}
.page--values{left:52px}
.page--partners{left:425px}
.page--contact{left:797px}
.abs{position:absolute}

/* values page */
.values-title{left:72px;top:57px;font-size:16px;font-weight:400;color:var(--ink-soft);letter-spacing:.5px}
.team-art{left:192px;top:12px;width:157px;height:67px;background:linear-gradient(180deg,#ff3b3b 0%,var(--red) 100%)}
.building-art{left:0;top:79px;width:68px;height:292px;background:linear-gradient(160deg,#9a9a9a 0%,#4a4a4a 45%,#1f1f1f 100%)}
.values-panel{left:68px;top:79px;width:283px;height:292px;background:var(--red)}
.value-word{left:95px;font-family:"Oswald","Arial Narrow",sans-serif;font-weight:700;text-transform:uppercase;line-height:1;white-space:nowrap;-webkit-background-clip:text;background-clip:text;color:transparent}
.value-word--integrity{top:116px;font-size:33px;letter-spacing:6.5px;background-image:linear-gradient(180deg,#f4f4f4,#9b9b9b)}
.value-word--accountability{top:151px;font-size:24px;letter-spacing:2.4px;background-image:linear-gradient(180deg,#cfcfcf,#6b6b6b)}
.value-word--respect{top:176px;font-size:38px;letter-spacing:9px;background-image:linear-gradient(180deg,#777,#2a2a2a)}
.value-word--team{top:218px;font-size:78px;letter-spacing:11px;background-image:linear-gradient(180deg,#5a5a5a,#1c1c1c)}
.value-word--work{top:293px;font-size:76px;letter-spacing:7px;background-image:linear-gradient(180deg,#4a4a4a,#111)}
.brand{display:flex;align-items:center;gap:5px;color:var(--red-deep);font-weight:400;white-space:nowrap}
.brand__mark{width:13px;height:13px;background:var(--red-deep)}
.brand--values{left:64px;top:389px;font-size:21px}
.values-blurb{left:64px;top:422px;width:250px;font-size:9.3px;line-height:13px;color:var(--ink);letter-spacing:-.1px}
.band-grey{left:0;top:479px;width:40px;height:18px;background:var(--grey-band)}
.band-red{left:40px;top:479px;width:311px;height:18px;background:var(--red)}

/* partners page */
.partners-title{left:44px;top:41px;font-size:13px;font-weight:400;color:var(--ink)}
.partners-title b{color:var(--red-deep);font-size:17px;font-weight:700}
.partner-band{left:0;width:327px;display:flex;align-items:center}
.partner-band--tech{top:60px;height:40px;background:var(--black)}
.partner-band--finance{top:100px;height:60px;background:var(--red)}
.partner-band__icon{width:70px;height:100%;display:flex;align-items:center;justify-content:center;border-right:1px solid rgba(255,255,255,.35)}
.partner-list{list-style:none;padding-left:12px}
.partner-list li{font-size:9.3px;line-height:16px;color:var(--white);position:relative;padding-left:13px;white-space:nowrap}
.partner-list li::before{content:"";position:absolute;left:0;top:5px;width:6px;height:6px;border-radius:50%;background:var(--red-deep)}
.partner-band--finance .partner-list li{color:#ffe6e6}
.partner-band--finance .partner-list li::before{background:#b10016}
.service-col{top:175px;width:81px;background:var(--panel-grey);height:66px}
.service-col__head{background:var(--grey-head);color:var(--white);font-size:7.8px;font-weight:700;padding:2px 3px;height:15px;line-height:11px;white-space:nowrap;letter-spacing:-.1px}
.service-col ul{list-style:none;padding:3px 4px}
.service-col li{font-size:7.4px;line-height:10px;color:var(--ink);padding-left:6px;position:relative}
.service-col li::before{content:"";position:absolute;left:0;top:3px;width:4px;height:4px;border-radius:50%;background:var(--red-deep)}
.service-col--dev{left:37px}
.service-col--consult{left:128px;width:88px}
.service-col--consult li{white-space:nowrap}
.service-col--invest{left:226px}
.sector{left:36px;width:265px}
.sector h3{font-size:12.5px;font-weight:700;color:var(--red-deep);line-height:15px}
.sector p{font-size:7.9px;line-height:12px;color:var(--ink);text-align:justify}
.sector--oil{top:254px}
.sector--power{top:306px}
.sector--renew{top:351px}
.partners-footer{left:0;top:427px;width:351px;height:70px;background:var(--black)}

/* contact page */
.contact-top{left:0;top:0;width:351px;height:160px;background:var(--charcoal)}
.contact-logo-box{left:65px;top:107px;width:195px;height:53px;background:var(--white)}
.brand--contact{left:80px;top:123px;font-size:23px}
.contact-tail{left:0;top:271px;width:351px;height:226px;background:var(--page-tail)}
.contact-card{left:60px;top:166px;width:230px;text-align:center;color:var(--ink);font-style:normal}
.contact-card__name{display:inline-block;background:#d6d6d6;font-size:10px;font-weight:700;padding:1px 10px;letter-spacing:.3px}
.contact-card__addr{font-size:8.2px;line-height:10.5px;margin-top:2px}
.contact-card__web{font-size:8.8px;line-height:12px;margin-top:5px}
.disclaimer{left:42px;top:404px;width:266px;font-size:4.3px;line-height:5.8px;color:#666;text-align:justify}
.disclaimer p+p{margin-top:4px}
</style>
</head>
<body>
<main class="canvas">

  <section class="page page--values">
    <div class="abs team-art" role="img" aria-label="Red silhouettes of a business team"></div>
    <h2 class="abs values-title">OUR VALUES</h2>
    <div class="abs building-art" role="img" aria-label="Black and white photo of a modern office building"></div>
    <div class="abs values-panel"></div>
    <span class="abs value-word value-word--integrity">Integrity</span>
    <span class="abs value-word value-word--accountability">Accountability</span>
    <span class="abs value-word value-word--respect">Respect</span>
    <span class="abs value-word value-word--team">Team</span>
    <span class="abs value-word value-word--work">Work</span>
    <div class="abs brand brand--values"><span class="brand__mark"></span>VeltHoldings</div>
    <p class="abs values-blurb">VeltHoldings partners with like-minded investors, project developers, and industry experts to create the greatest value in all its transactions.</p>
    <div class="abs band-grey"></div>
    <div class="abs band-red"></div>
  </section>

  <section class="page page--partners">
    <h2 class="abs partners-title">Valued <b>Partnerships</b></h2>
    <div class="abs partner-band partner-band--tech">
      <div class="partner-band__icon">
        <svg width="34" height="24" viewBox="0 0 34 24" aria-hidden="true">
          <rect x="14" y="4" width="16" height="18" fill="none" stroke="#fff" stroke-width="1.5"/>
          <line x1="17" y1="9" x2="27" y2="9" stroke="#fff" stroke-width="1.3"/>
          <line x1="17" y1="13" x2="27" y2="13" stroke="#fff" stroke-width="1.3"/>
          <line x1="17" y1="17" x2="27" y2="17" stroke="#fff" stroke-width="1.3"/>
          <circle cx="9" cy="9" r="6" fill="none" stroke="#ff0000" stroke-width="2"/>
          <line x1="5" y1="13" x2="1" y2="18" stroke="#ff0000" stroke-width="2.5"/>
        </svg>
      </div>
      <ul class="partner-list">
        <li>Globally renowned and leading local Technical Partners</li>
        <li>Foreign and local Legal Counsel</li>
      </ul>
    </div>
    <div class="abs partner-band partner-band--finance">
      <div class="partner-band__icon">
        <svg width="30" height="26" viewBox="0 0 30 26" aria-hidden="true">
          <circle cx="19" cy="10" r="8" fill="#fff" stroke="#000" stroke-width="1"/>
          <text x="19" y="14" font-size="11" font-weight="700" text-anchor="middle" font-family="Arimo,Arial,sans-serif" fill="#000">$</text>
          <circle cx="9" cy="17" r="7" fill="#000"/>
          <text x="9" y="21" font-size="10" font-weight="700" text-anchor="middle" font-family="Arimo,Arial,sans-serif" fill="#fff">$</text>
        </svg>
      </div>
      <ul class="partner-list">
        <li>Development Finance Institutions</li>
        <li>International Commercial Banks</li>
        <li>Local Commercial Banks</li>
      </ul>
    </div>

    <div class="abs service-col service-col--dev">
      <div class="service-col__head">Project development</div>
      <ul><li>Deal Origination</li><li>Project Structuring</li><li>PPP Advisory</li></ul>
    </div>
    <div class="abs service-col service-col--consult">
      <div class="service-col__head">Consulting</div>
      <ul><li>Strategic planning</li><li>Business Planning</li><li>Financial Advisory</li><li>Process Improvement</li></ul>
    </div>
    <div class="abs service-col service-col--invest">
      <div class="service-col__head">Investment</div>
      <ul><li>Incubation</li><li>Due Diligence</li><li>Fund-raising</li><li>Portfolio Company Supplementation</li></ul>
    </div>

    <article class="abs sector sector--oil">
      <h3>Oil &amp; Gas</h3>
      <p>Service Provider for an indigenous oil &amp; gas development company contracted by the Nigerian Government to promote industrial development around the oil &amp; gas sector</p>
    </article>
    <article class="abs sector sector--power">
      <h3>Conventional Power</h3>
      <p>Financial Adviser to a local power company developing a thermal power plant to boost national generating capacity</p>
    </article>
    <article class="abs sector sector--renew">
      <h3>Renewables/ Cleantech</h3>
      <p>West Africa Adviser and Service Provider to an international specialized fund manager investing in renewable energy and clean technology projects across Africa</p>
    </article>
    <div class="abs partners-footer"></div>
  </section>

  <section class="page page--contact">
    <div class="abs contact-top"></div>
    <div class="abs contact-logo-box"></div>
    <div class="abs brand brand--contact"><span class="brand__mark"></span>VeltHoldings</div>
    <div class="abs contact-tail"></div>
    <address class="abs contact-card">
      <div class="contact-card__name">VELTHOLDINGS LIMITED</div>
      <div class="contact-card__addr">14 Harbour Crest Lane<br>Off Marina Close<br>East Quarter<br>Lagos, Nigeria</div>
      <div class="contact-card__web">E mail: info@veltholdings-grp.net<br>Web: http://www.veltholdings-grp.net</div>
    </address>
    <div class="abs disclaimer">
      <p>Veltmoor Capital and Holdings Limited (VeltHoldings) accepts no responsibility for any improper or incorrect use of the information contained herein. Under no circumstances shall VeltHoldings be liable for any actions taken or omissions made in reliance on any information contained herein from whatever source, nor shall VeltHoldings be liable for any other consequences arising from such reliance. In no event shall VeltHoldings be held liable for any direct, indirect, incidental, special or consequential damages however caused and on any theory of liability arising in any way out of the use of this information.</p>
      <p>Information or opinions provided in this document do not constitute an offer to sell or a solicitation of an offer to buy any securities or financial instruments, or any advice or recommendation with respect to such securities or instruments.</p>
    </div>
  </section>

</main>
</body>
</html>
```